Business Card Design for a Technology Development Company

******* PLEASE NOTE (ALL DESIGNERS): I am going to finish the competition on Monday the 9th July (NOT SATURDAY 15TH). I have some designs I like and need to get them printed next week. Please submit any designs today or tomorrow. *******

PLEASE READ ALL OF THE REQUIREMENTS!!! I've rejected lot's of designs in the past because they didn't read the basic requirements - thanks and good luck!

Quill Harbor is a UK technology / small holding company that invests in startups and develops new ideas. In addition it provides IT Professional Services.

Ideally the design will be simple, professional, smart, and sophisticated, and overall be nice to look at. You can be creative as you like with the design, equally as simple as you like - you guys are the professionals so I'll leave it to your inspiration (make sure you incorporate the logo)!
Updates

PLEASE NOTE (ALL DESIGNERS): I am going to finish the competition on Monday the 9th July (NOT SATURDAY 15TH).  I have some designs I like and need to get them printed next week.  Please submit any designs today or tomorrow.

Target Market(s)

Enterprises / corporations / public sector / technical engineers / investors. More www.brantelix.com / www.vornel.com than www.pibbleroo.com!

Industry/Entity Type

Business

Requirements
Must have
• It should be modern and any artwork (if used) should be simple
- Pastel colours, dark and light colours, and shades are preferred over bright colours
- The design should incorporate the attached Quill Harbor logo and the logo colour scheme
- The logo should be on both sides. The back should just have the logo, maybe with some additional graphics
- It must have the following information on:

FirstName SecondName
Company Position
Email: name@quillharbor.co.uk
Mobile: +44 (0) 7700 984312

- The final design should be for a UK business card, dimensions: 85mm × 55mm
- The final design should have bleed marks to allow for printing and should be given in vector formats (EPS and AI)
Nice to have
• The Logo can be separated from the font in the logo on the front of the card. This isn't necessary or required, just to know it's not a limitation.
Should not have
• No bright colours (I prefer pastel colours, dark and light colours, and shades)
- Fonts that are to thin
- Effects or designs that make it difficult to print
- Italic or old fashioned looking fonts, i.e. anything like Times New Roman is a NO!

```html
<!DOCTYPE html>
<html lang="en">
<head>
<meta charset="utf-8">
<title>Quill Harbor – Business Card</title>
<link href="https://fonts.googleapis.com/css2?family=Jost:wght@400;500;600&display=swap" rel="stylesheet">
<style>
  :root {
    --page-bg: #eef1f2;
    --card-white: #ffffff;
    --band-blue: #84c6d4;
    --brand-teal: #17727f;
    --brand-light: #6cbccb;
    --text-on-band: #ffffff;
    --card-shadow: rgba(20, 40, 50, 0.18);
  }
  * { margin: 0; padding: 0; box-sizing: border-box; }
  html, body {
    width: 1200px;
    height: 1000px;
    overflow: hidden;
    background: var(--page-bg);
    font-family: "Jost", "Futura", sans-serif;
  }
  .card-sheet {
    position: relative;
    width: 1200px;
    height: 1000px;
  }
  .card {
    position: absolute;
    top: 332px;
    width: 520px;
    height: 336px;
    background: var(--card-white);
    box-shadow: 0 6px 18px var(--card-shadow);
    overflow: hidden;
  }
  .card--back { left: 60px; }
  .card--front { left: 620px; }

  .card__band {
    position: absolute;
    left: 0;
    right: 0;
    bottom: 0;
    background: var(--band-blue);
  }
  .card--back .card__band { height: 46%; }
  .card--front .card__band { height: 60%; }

  /* Back: brand name centred in white area */
  .brand-lockup {
    position: absolute;
    left: 0;
    right: 0;
    top: 120px;
    display: flex;
    align-items: center;
    justify-content: center;
    gap: 14px;
  }
  .brand-lockup__dot {
    width: 44px;
    height: 44px;
    border-radius: 50%;
    background: var(--brand-teal);
  }
  .brand-lockup__name {
    font-size: 36px;
    font-weight: 600;
    color: var(--brand-teal);
    letter-spacing: 0.5px;
  }

  /* Front: mark position and contact details */
  .front-mark {
    position: absolute;
    left: 70px;
    top: 94px;
    width: 96px;
    height: 96px;
    border-radius: 50%;
    background: var(--brand-teal);
  }
  .person {
    position: absolute;
    left: 238px;
    top: 58px;
  }
  .person__name {
    font-size: 19px;
    font-weight: 600;
    color: var(--brand-teal);
    line-height: 1.2;
  }
  .person__role {
    font-size: 16px;
    font-weight: 400;
    color: var(--brand-light);
    line-height: 1.3;
    margin-left: 12px;
  }
  .contact {
    position: absolute;
    left: 278px;
    top: 168px;
    list-style: none;
    color: var(--text-on-band);
    font-size: 16px;
    font-weight: 500;
    line-height: 1.35;
  }
  .contact__phone { margin-left: 10px; }
</style>
</head>
<body>
  <main class="card-sheet">
    <section class="card card--back" aria-label="Card back">
      <div class="card__band"></div>
      <div class="brand-lockup">
        <span class="brand-lockup__dot"></span>
        <span class="brand-lockup__name">Quill Harbor</span>
      </div>
    </section>

    <section class="card card--front" aria-label="Card front">
      <div class="card__band"></div>
      <span class="front-mark"></span>
      <div class="person">
        <p class="person__name">Employees Name</p>
        <p class="person__role">Employees Position</p>
      </div>
      <ul class="contact">
        <li class="contact__email">name@quillharbor.co.uk</li>
        <li class="contact__phone">+44 (0) 7700 984312</li>
      </ul>
    </section>
  </main>
</body>
</html>
```